Dental Co needs single page print ad

Dental company needs a 1 page ad for trade magazines.
I am uploading an example of what we want (words). We need you to make it look great. It can include people or not.
The uploaded ad isn't there to be copied, just to kind of frame what we are thinking. We are open to any design
One page ad
Size 1)

Trim Size - 8 x 10.5
Bleed Size - 8.25 x 10.75
Live Area - 7 x 10

Size 2)

Trim - 8 x 10.875
Bleed - 8.25 x 11.125
Live Area - 7 x 9.875

BRIX Brand Hex #'s

Orange - ff6319
Teal - 56b1bf
Lt. Teal - aed9da
Blue: #38394B

Target Market(s)

Dentists

Requirements
Must have
• BRIX Logo, pic of the sensor (called VANT)
Use the brand hex colors:
Orange - ff6319
Teal - 56b1bf
Lt. Teal - aed9da
Blue: #38394B

```html
<!DOCTYPE html>
<html lang="en">
<head>
<meta charset="utf-8">
<title>VANT Subscription Ad – BRIX Imaging</title>
<link rel="stylesheet" href="https://fonts.googleapis.com/css2?family=Montserrat:wght@400;500;800;900&family=Oswald:wght@500;600&display=swap">
<style>
  :root {
    --navy: #2b2e83;
    --orange: #f26522;
    --white: #ffffff;
    --grey-mid: #9a9a9a;
    --skin-light: #f3d6c6;
    --skin-mid: #e6b8a0;
    --skin-deep: #c98e72;
    --sensor-dark: #2a2c45;
    --sensor-mid: #4a4d6e;
  }
  * { box-sizing: border-box; margin: 0; padding: 0; }
  html, body { width: 800px; height: 1200px; overflow: hidden; background: var(--white); }
  .ad {
    position: relative; width: 800px; height: 1200px; overflow: hidden;
    background: var(--white);
    font-family: "Montserrat", Arial, sans-serif; color: var(--navy);
  }
  .hero-shade {
    position: absolute; left: 0; top: 330px; width: 800px; height: 300px;
    background: linear-gradient(180deg, var(--white) 0%, #d9d9d9 55%, var(--grey-mid) 100%);
  }
  .hero-photo {
    position: absolute; left: 432px; top: 0; width: 368px; height: 630px;
    background: radial-gradient(ellipse at 60% 35%, var(--skin-light) 0%, var(--skin-mid) 55%, var(--skin-deep) 100%);
  }
  .product-name {
    position: absolute; left: 58px; top: 50px;
    font-weight: 900; font-size: 78px; letter-spacing: 1px; line-height: 1;
  }
  .headline {
    position: absolute; left: 60px; top: 172px; width: 370px;
    font-weight: 800; font-size: 31px; line-height: 37px; text-transform: uppercase;
  }
  .headline .aside {
    display: block; text-transform: none; color: var(--orange); font-size: 27px;
  }
  .sensor-photo {
    position: absolute; left: 58px; top: 388px; width: 312px; height: 272px;
    border-radius: 40px;
    background: linear-gradient(160deg, var(--sensor-mid) 0%, var(--sensor-dark) 100%);
    box-shadow: 0 10px 18px rgba(0,0,0,.35);
  }
  .price { position: absolute; left: 58px; width: 380px; height: 160px; }
  .price--setup { top: 672px; }
  .price--monthly { top: 843px; }
  .price svg { position: absolute; left: 0; top: 0; }
  .price-amount {
    position: absolute; left: 22px; top: 14px; width: 230px; height: 126px;
    display: flex; align-items: center; justify-content: center;
    font-family: "Oswald", "Arial Narrow", sans-serif; font-weight: 600; font-size: 72px;
    color: var(--white); line-height: 1;
  }
  .price-amount sup { font-size: 38px; align-self: flex-start; margin-top: 22px; margin-right: 6px; }
  .price-note {
    position: absolute; left: 231px; top: 0; width: 144px; height: 160px;
    display: flex; align-items: center; justify-content: center; text-align: center;
    color: var(--white); font-size: 19px; font-weight: 500; line-height: 25px;
  }
  .benefits {
    position: absolute; left: 480px; top: 696px; width: 310px; list-style: none;
  }
  .benefits li {
    position: relative; padding-left: 34px; height: 58px;
    font-size: 17px; font-weight: 500; line-height: 19px;
  }
  .benefits svg { position: absolute; left: 0; top: 1px; }
  .brand-name {
    position: absolute; left: 60px; top: 1040px;
    font-weight: 900; font-size: 36px; line-height: 40px; letter-spacing: 1px;
  }
  .contact { position: absolute; left: 305px; top: 1036px; }
  .contact-line { display: flex; align-items: center; gap: 12px; white-space: nowrap; }
  .contact-line--phone { font-weight: 800; font-size: 40px; line-height: 48px; }
  .contact-line--web { font-weight: 500; font-size: 25px; margin-top: 8px; }
  .footer-band {
    position: absolute; left: 0; bottom: 0; width: 800px; height: 26px; background: var(--orange);
  }
</style>
</head>
<body>
<main class="ad">
  <div class="hero-shade"></div>
  <div class="hero-photo" role="img" aria-label="Photo of a smiling woman's lower face and hand, cropped at the top right"></div>

  <h1 class="product-name">VANT</h1>
  <h2 class="headline">A subscription<br>option for<br>intra-oral<br>sensors is dumb <span class="aside">(Until you do the math)</span></h2>

  <div class="sensor-photo" role="img" aria-label="Product photo of the VANT intra-oral sensor with its cable"></div>

  <div class="price price--setup">
    <svg width="380" height="160" viewBox="0 0 380 160">
      <polygon points="0,17 270,17 270,143 0,143 20,80" fill="var(--orange)"/>
      <polygon points="303,0 375,40 375,120 303,160 231,120 231,40" fill="var(--navy)"/>
    </svg>
    <div class="price-amount"><sup>$</sup>1,999</div>
    <div class="price-note">One-time<br>sign up fee</div>
  </div>

  <div class="price price--monthly">
    <svg width="380" height="160" viewBox="0 0 380 160">
      <polygon points="0,17 270,17 270,143 0,143 20,80" fill="var(--orange)"/>
      <polygon points="303,0 375,40 375,120 303,160 231,120 231,40" fill="var(--navy)"/>
    </svg>
    <div class="price-amount"><sup>$</sup>139</div>
    <div class="price-note">Per<br>Mo-cancel<br>anytime</div>
  </div>

  <ul class="benefits">
    <li><svg width="18" height="18" viewBox="0 0 18 18"><circle cx="9" cy="9" r="7.5" fill="none" stroke="var(--navy)" stroke-width="1.5"/><path d="M5 9.5l3 3 6-7" fill="none" stroke="var(--navy)" stroke-width="1.6"/></svg>Lifetime $0 deductible<br>warranty</li>
    <li><svg width="18" height="18" viewBox="0 0 18 18"><circle cx="9" cy="9" r="7.5" fill="none" stroke="var(--navy)" stroke-width="1.5"/><path d="M5 9.5l3 3 6-7" fill="none" stroke="var(--navy)" stroke-width="1.6"/></svg>Unlimited support &amp;<br>upgrades</li>
    <li><svg width="18" height="18" viewBox="0 0 18 18"><circle cx="9" cy="9" r="7.5" fill="none" stroke="var(--navy)" stroke-width="1.5"/><path d="M5 9.5l3 3 6-7" fill="none" stroke="var(--navy)" stroke-width="1.6"/></svg>Direct integration w/all<br>major software</li>
    <li><svg width="18" height="18" viewBox="0 0 18 18"><circle cx="9" cy="9" r="7.5" fill="none" stroke="var(--navy)" stroke-width="1.5"/><path d="M5 9.5l3 3 6-7" fill="none" stroke="var(--navy)" stroke-width="1.6"/></svg>Affordable enough for<br>every op</li>
    <li><svg width="18" height="18" viewBox="0 0 18 18"><circle cx="9" cy="9" r="7.5" fill="none" stroke="var(--navy)" stroke-width="1.5"/><path d="M5 9.5l3 3 6-7" fill="none" stroke="var(--navy)" stroke-width="1.6"/></svg>Preserve your capital</li>
  </ul>

  <div class="brand-name">BRIX<br>IMAGING</div>

  <div class="contact">
    <div class="contact-line contact-line--phone">
      <svg width="24" height="24" viewBox="0 0 24 24"><path d="M6.6 10.8a15 15 0 0 0 6.6 6.6l2.2-2.2a1 1 0 0 1 1-.25 11.4 11.4 0 0 0 3.6.57 1 1 0 0 1 1 1V20a1 1 0 0 1-1 1A17 17 0 0 1 3 4a1 1 0 0 1 1-1h3.5a1 1 0 0 1 1 1c0 1.25.2 2.45.57 3.57a1 1 0 0 1-.25 1z" fill="var(--orange)"/></svg>
      (555) 014-2749
    </div>
    <div class="contact-line contact-line--web">
      <svg width="24" height="24" viewBox="0 0 24 24"><circle cx="12" cy="12" r="10" fill="var(--orange)"/><path d="M2 12h20M12 2c3 3 3 17 0 20M12 2c-3 3-3 17 0 20" fill="none" stroke="var(--white)" stroke-width="1.3"/></svg>
      www.brixsensors.example
    </div>
  </div>

  <div class="footer-band"></div>
</main>
</body>
</html>
```